Brightline Leads needs a business card

The drawer sage is a lead generation service serving the Custom Closet industry.

Here is the basic card information:

Brightline Leads
Gregory Tessman
Owner/CEO
Fairbrook, OR
503-555-0183 Cell
Email: gtessman@BrightlineLeads.example

Additional information for the card:

"High quality, flat rate lead generation exclusively for the custom closet industry"

Bullet points for the back:

- Low fixed cost
- Easy to budget
- Guaranteed qualified Leeds
- Exclusivity per city

Logo attached, head shot attached. Photos of closet systems attached

```html
<!DOCTYPE html>
<html lang="en">
<head>
<meta charset="utf-8">
<title>Brightline Leads – Business Card</title>
<link href="https://fonts.googleapis.com/css2?family=Poppins:wght@500;600;700&family=Sorts+Mill+Goudy&family=Great+Vibes&display=swap" rel="stylesheet">
<style>
  :root{
    --page:#e7e6e7;
    --brown-dark:#3f220f;
    --copper:#a5592a;
    --copper-light:#c7814a;
    --tan:#b9733f;
    --white:#ffffff;
    --cream:#f3ece4;
    --icon-line:#6b3d1d;
  }
  *{margin:0;padding:0;box-sizing:border-box}
  html,body{width:1200px;height:2297px;overflow:hidden;background:var(--page)}
  body{position:relative;font-family:"Poppins",sans-serif}

  .card{position:absolute;left:129px;width:941px;height:537px;overflow:hidden;background:var(--brown-dark)}
  .card--back{top:967px}
  .card--front{top:1621px}

  /* back side */
  .back-brand{position:absolute;left:0;top:0;width:486px;height:100%;
    background:linear-gradient(180deg,#44260f 0%,var(--brown-dark) 60%,#3a1f0d 100%);text-align:center}
  .back-benefits{position:absolute;left:486px;top:0;right:0;height:100%;
    background:linear-gradient(180deg,#a65b27 0%,var(--copper) 55%,#9a5222 100%)}
  .brand-name{position:absolute;font-family:"Poppins",sans-serif;font-weight:600;color:var(--white);white-space:nowrap}
  .back-brand .brand-name{left:0;right:0;top:226px;font-size:40px;line-height:48px}
  .dots{position:absolute;left:0;right:0;top:300px;color:var(--white);font-size:26px;letter-spacing:3px;font-weight:700;line-height:1}
  .tagline{position:absolute;left:0;right:0;top:336px;color:var(--copper-light);font-weight:700;font-size:24px;line-height:31px}
  .tagline-script{position:absolute;left:0;right:0;top:398px;color:var(--cream);font-family:"Great Vibes",cursive;font-size:36px;line-height:36px}

  .benefit{position:absolute;left:68px;display:flex;align-items:center;gap:20px;color:var(--white);font-weight:500;font-size:25px;line-height:31px}
  .benefit-icon{width:61px;height:61px;border-radius:50%;background:var(--white);flex:none;box-shadow:0 3px 6px rgba(0,0,0,.3);display:flex;align-items:center;justify-content:center}
  .benefit-icon svg{width:38px;height:38px}
  .divider{position:absolute;left:71px;width:302px;border-top:1px dashed rgba(60,28,8,.7)}

  /* front side */
  .front-band{position:absolute;left:0;right:0;top:418px;bottom:0;background:linear-gradient(180deg,#a65b27,#9a5222)}
  .headshot{position:absolute;left:127px;top:60px;width:163px;height:163px;border:2px solid var(--tan);
    background:linear-gradient(160deg,#2b2d33 0%,#3d3f46 55%,#23262c 100%)}
  .person-name{position:absolute;left:0;width:416px;top:236px;text-align:center;font-family:"Sorts Mill Goudy",serif;color:var(--copper-light);font-size:40px;line-height:46px}
  .person-role{position:absolute;left:0;width:416px;top:282px;text-align:center;font-family:"Sorts Mill Goudy",serif;color:var(--white);font-size:24px;letter-spacing:5px}
  .card--front .brand-name{left:440px;top:140px;font-size:34px;line-height:42px}
  .contact{position:absolute;left:440px;list-style:none}
  .contact li{position:absolute;left:0;display:flex;align-items:center;gap:12px;color:var(--white);font-weight:500;font-size:23px;white-space:nowrap;height:30px}
  .contact svg{width:22px;height:22px;flex:none}
  .gallery-photo{position:absolute;top:358px;width:193px;height:118px;border:2px solid var(--tan)}
</style>
</head>
<body>

<section class="card card--back" aria-label="Business card back">
  <div class="back-brand">
    <div class="brand-name">Brightline Leads</div>
    <div class="dots">••••••</div>
    <p class="tagline">High quality, flat rate<br>lead generation</p>
    <p class="tagline-script">Exclusively for the custom<br>closet industry.</p>
  </div>
  <div class="back-benefits">
    <div class="benefit" style="top:83px">
      <span class="benefit-icon"><svg viewBox="0 0 40 40" fill="none" stroke="var(--icon-line)" stroke-width="2"><circle cx="17" cy="20" r="9"/><path d="M17 15v10M20 17h-4a2 2 0 0 0 0 4h2a2 2 0 0 1 0 4h-4"/><path d="M29 10v18l-4-4M29 28l4-4"/></svg></span>
      <span>Low fixed cost</span>
    </div>
    <div class="divider" style="top:161px"></div>
    <div class="benefit" style="top:177px">
      <span class="benefit-icon"><svg viewBox="0 0 40 40" fill="none" stroke="var(--icon-line)" stroke-width="2"><circle cx="21" cy="19" r="11"/><path d="M21 8v11h11M21 19l-8 8"/><rect x="6" y="25" width="8" height="8"/></svg></span>
      <span>Easy to budget</span>
    </div>
    <div class="divider" style="top:261px"></div>
    <div class="benefit" style="top:271px">
      <span class="benefit-icon"><svg viewBox="0 0 40 40" fill="none" stroke="var(--icon-line)" stroke-width="2"><path d="M20 11h-6a9 9 0 0 0 0 18h6v-5h-6a4 4 0 0 1 0-8h6z"/><circle cx="29" cy="13" r="2.5"/><circle cx="29" cy="27" r="2.5"/><path d="M33 11h3M33 15h3M33 25h3M33 29h3"/></svg></span>
      <span>Guaranteed<br>qualified Leeds</span>
    </div>
    <div class="divider" style="top:372px"></div>
    <div class="benefit" style="top:395px">
      <span class="benefit-icon"><svg viewBox="0 0 40 40" fill="none" stroke="var(--icon-line)" stroke-width="2"><circle cx="20" cy="16" r="11"/><circle cx="20" cy="16" r="7"/><path d="M20 12l1.5 3h3l-2.4 2 1 3-3.1-1.8-3.1 1.8 1-3-2.4-2h3z"/><path d="M13 25l-4 9 4-1 2 3 3-8M27 25l4 9-4-1-2 3-3-8"/></svg></span>
      <span>Exclusivity per city</span>
    </div>
  </div>
</section>

<section class="card card--front" aria-label="Business card front">
  <div class="front-band"></div>
  <div class="headshot" role="img" aria-label="Headshot portrait of Gregory Tessman"></div>
  <div class="person-name">Gregory Tessman</div>
  <div class="person-role">OWNER/CEO</div>

  <div class="brand-name">Brightline Leads</div>
  <ul class="contact">
    <li style="top:203px"><svg viewBox="0 0 24 24"><path fill="var(--copper)" d="M12 2a7 7 0 0 0-7 7c0 5 7 13 7 13s7-8 7-13a7 7 0 0 0-7-7zm0 9.5A2.5 2.5 0 1 1 12 6.5a2.5 2.5 0 0 1 0 5z"/></svg>Fairbrook, OR</li>
    <li style="top:239px"><svg viewBox="0 0 24 24"><circle cx="12" cy="12" r="11" fill="var(--copper)"/><path fill="var(--brown-dark)" d="M8.5 6.5l2 2-1.2 1.6a7 7 0 0 0 4.6 4.6l1.6-1.2 2 2-1.3 1.8C11.5 17 7 12.5 6.7 7.8z"/></svg>503-555-0183</li>
    <li style="top:276px"><svg viewBox="0 0 24 24"><circle cx="12" cy="12" r="11" fill="var(--copper)"/><rect x="6.5" y="8" width="11" height="8" fill="none" stroke="var(--brown-dark)" stroke-width="1.5"/><path d="M6.5 8l5.5 4.5L17.5 8" fill="none" stroke="var(--brown-dark)" stroke-width="1.5"/></svg>gtessman@BrightlineLeads.example</li>
  </ul>

  <div class="gallery-photo" style="left:54px;background:linear-gradient(180deg,#3a2a22 0%,#b8664a 45%,#d7c9a8 100%)" role="img" aria-label="Photo of a garage cabinet system"></div>
  <div class="gallery-photo" style="left:261px;background:linear-gradient(180deg,#8aa4c2 0%,#b6c3d3 55%,#6f7a86 100%)" role="img" aria-label="Photo of a laundry and storage room"></div>
  <div class="gallery-photo" style="left:467px;background:linear-gradient(180deg,#d9dbe0 0%,#b9796f 50%,#efe9e5 100%)" role="img" aria-label="Photo of a walk-in closet"></div>
  <div class="gallery-photo" style="left:674px;background:linear-gradient(180deg,#2a2725 0%,#8f7a66 45%,#e8e6e2 100%)" role="img" aria-label="Photo of a home office with built-in shelving"></div>
</section>

</body>
</html>
```